New "above the fold" design for our website

We would like to see some new creative designs for our above the fold section on our homepage. We are an online marketplace for fresh produce and meat.

You must design the desktop and mobile layouts.

Target Market(s)

Women 30-45 years old who buy groceries, with 2 children under 10 years old.

Industry/Entity Type

Grocery Store

Number of Pages Required

1 page

Font styles to use
Sans Serif

Requirements
Must have
• Give customers the sense of organic and farm fresh as we are battling the big supermarket chains.
Nice to have
• Pictures of produce. Pictures of farmers.

```html
<!DOCTYPE html>
<html lang="en">
<head>
<meta charset="utf-8">
<title>Fieldhand – Quality Meat &amp; Produce</title>
<link rel="stylesheet" href="https://fonts.googleapis.com/css2?family=Lato:wght@300;400;700;900&display=swap">
<style>
  :root {
    --green: #8aae2e;
    --green-dark: #6e8f1f;
    --green-light: #a3c93a;
    --lime: #b5cf2a;
    --orange: #f6b21c;
    --orange-dark: #e79f0c;
    --text: #4a4a4a;
    --muted: #7a7a7a;
    --line: #e2e2e2;
    --footer-bg: #f2f6e2;
    --footer-text: #5c6b2a;
    --white: #ffffff;
  }
  * { box-sizing: border-box; margin: 0; padding: 0; }
  html, body { width: 1200px; height: 720px; overflow: hidden; background: var(--white); }
  body { font-family: 'Lato', sans-serif; color: var(--text); position: relative; }

  .site-header { position: absolute; left: 0; top: 0; width: 1200px; height: 70px; border-bottom: 1px solid var(--line); background: var(--white); }
  .brand { position: absolute; left: 232px; top: 12px; width: 154px; height: 76px; background: var(--green); border-radius: 12px; border: 3px solid #c7dc8c; display: flex; align-items: center; justify-content: center; z-index: 5; }
  .brand-name { color: var(--white); font-weight: 700; font-size: 17px; letter-spacing: 1px; }
  .main-nav a { position: absolute; top: 27px; font-size: 11px; color: var(--footer-text); text-decoration: none; transform: translateX(-50%); }
  .main-nav .sep { position: absolute; top: 28px; width: 1px; height: 15px; background: var(--line); }
  .btn-register { position: absolute; left: 697px; top: 21px; width: 96px; height: 29px; border: 1px solid var(--line); border-radius: 2px; font-size: 11px; color: var(--footer-text); display: flex; align-items: center; justify-content: center; }
  .btn-login { position: absolute; left: 873px; top: 21px; width: 96px; height: 29px; background: var(--orange); border-radius: 2px; color: var(--white); font-size: 11px; display: flex; align-items: center; justify-content: center; gap: 6px; }

  .hero-photo { position: absolute; left: 158px; top: 70px; width: 883px; height: 358px;
    background: radial-gradient(circle at 80% 10%, #d97a22 0, transparent 22%),
                radial-gradient(circle at 20% 20%, #c9a03a 0, transparent 25%),
                radial-gradient(circle at 70% 80%, #a3221a 0, transparent 35%),
                linear-gradient(160deg, #5b4a2a 0%, #3e5a2a 40%, #7a2a1e 75%, #4a3a22 100%); }
  .headline-band { position: absolute; left: 413px; top: 154px; width: 628px; height: 102px; background: rgba(138, 174, 46, 0.92); }
  .bio-mark { position: absolute; left: 440px; top: 172px; width: 56px; height: 64px; background: rgba(40, 50, 20, 0.25); border-radius: 4px; }
  .headline-kicker { position: absolute; left: 522px; top: 168px; font-weight: 300; font-size: 21px; color: #3d4a1a; }
  .headline-main { position: absolute; left: 521px; top: 194px; font-weight: 700; font-size: 40px; color: var(--white); }

  .since-field { position: absolute; left: 521px; top: 281px; width: 158px; height: 32px; border: 1px solid rgba(255,255,255,0.35); border-radius: 2px; color: var(--white); font-weight: 700; font-size: 12px; display: flex; align-items: center; justify-content: center; }
  .btn-shop { position: absolute; left: 702px; top: 281px; width: 158px; height: 32px; background: var(--orange); border-radius: 2px; color: var(--white); font-weight: 700; font-size: 12px; display: flex; align-items: center; justify-content: center; gap: 10px; }

  .farmer-photo { position: absolute; left: 232px; top: 148px; width: 168px; height: 399px; background: linear-gradient(180deg, #d8b49a 0%, #f2f2f2 30%, #2a3a6a 55%, #25335e 100%); border-radius: 60px 60px 0 0; z-index: 2; }

  .stat-card { position: absolute; top: 394px; width: 122px; height: 129px; background: var(--white); border: 1px solid #e6e6e6; border-bottom: 2px solid #d8d8d8; text-align: center; z-index: 3; }
  .stat-card svg { position: absolute; left: 47px; top: 20px; }
  .stat-value { position: absolute; left: 0; right: 0; top: 68px; font-size: 19px; font-weight: 700; color: #2a2a2a; }
  .stat-label { position: absolute; left: 0; right: 0; top: 96px; font-size: 11px; font-weight: 400; color: var(--muted); }

  .farms-band { position: absolute; left: 0; top: 547px; width: 1200px; height: 113px; border-top: 1px solid var(--line); }
  .natural-badge { position: absolute; left: 230px; top: 27px; width: 60px; height: 60px; border-radius: 50%; background: #4f9a2a; }
  .farms-title { position: absolute; left: 314px; top: 32px; font-weight: 300; font-size: 20px; color: #6f8a2a; }
  .farms-points { position: absolute; left: 314px; top: 69px; font-size: 8.5px; color: var(--lime); display: flex; gap: 12px; list-style: none; }
  .farms-points li + li::before { content: "•"; color: #cfcfcf; margin-right: 12px; }
  .butcher-photo { position: absolute; left: 820px; top: -35px; width: 148px; height: 148px; background: linear-gradient(180deg, #d6b69c 0%, #b9bcc2 35%, #f4f4f4 60%, #a8333a 80%, #f0f0f0 100%); border-radius: 70px 70px 0 0; }

  .site-footer { position: absolute; left: 0; top: 660px; width: 1200px; height: 60px; background: var(--footer-bg); border-top: 1px solid #dfe5c8; }
  .footer-nav { position: absolute; left: 232px; top: 26px; display: flex; list-style: none; font-size: 8px; font-weight: 700; color: var(--footer-text); }
  .footer-nav li { padding: 0 23px; border-left: 1px solid #d4dbb6; }
  .footer-nav li:first-child { padding-left: 0; border-left: none; }
  .copyright { position: absolute; right: 231px; top: 26px; font-size: 8px; color: #a0a47a; }
</style>
</head>
<body>
  <header class="site-header">
    <div class="brand"><span class="brand-name">FIELDHAND</span></div>
    <nav class="main-nav">
      <a href="#" style="left:480px">How it works</a>
      <span class="sep" style="left:549px"></span>
      <a href="#" style="left:603px">About</a>
      <span class="sep" style="left:657px"></span>
      <span class="sep" style="left:833px"></span>
    </nav>
    <div class="btn-register">Register</div>
    <div class="btn-login">
      <svg width="10" height="12" viewBox="0 0 10 12" fill="none" stroke="#fff" stroke-width="1.2"><rect x="1" y="5" width="8" height="6" rx="1"/><path d="M3 5V3.5a2 2 0 0 1 4 0V5"/></svg>
      Login
    </div>
  </header>

  <div class="hero-photo" role="img" aria-label="Photo of fresh vegetables: corn, carrots, tomatoes, onions and pumpkin"></div>
  <div class="headline-band"></div>
  <div class="bio-mark" role="img" aria-label="Hand-lettered 100% organic mark"></div>
  <p class="headline-kicker">Quality Meat &amp; Produce</p>
  <h1 class="headline-main">Delivered to your Door</h1>

  <div class="since-field">2010</div>
  <div class="btn-shop">
    <svg width="14" height="12" viewBox="0 0 14 12" fill="none" stroke="#fff" stroke-width="1.1"><path d="M1 1h2l1.5 7h7l1.5-5H4"/><circle cx="5.5" cy="10.5" r="0.9"/><circle cx="10.5" cy="10.5" r="0.9"/></svg>
    Shop now
  </div>

  <div class="farmer-photo" role="img" aria-label="Photo of a smiling butcher in a striped apron with arms crossed"></div>

  <section class="stats">
    <div class="stat-card" style="left:413px">
      <svg width="28" height="32" viewBox="0 0 28 32" fill="none" stroke="#a3c93a" stroke-width="1.5"><rect x="3" y="4" width="22" height="26" rx="2"/><path d="M9 2v4M14 2v4M19 2v4M7 13l2 2 3-3M15 14h6M7 20h2M15 20h6M7 25h2M15 25h6"/></svg>
      <div class="stat-value">34482</div><div class="stat-label">Orders</div>
    </div>
    <div class="stat-card" style="left:557px">
      <svg width="28" height="32" viewBox="0 0 28 32" fill="none" stroke="#a3c93a" stroke-width="1.5"><circle cx="6" cy="5" r="2.5"/><circle cx="14" cy="5" r="2.5"/><circle cx="22" cy="5" r="2.5"/><path d="M3 20v-8h6v8M11 30V12h6v18M19 20v-8h6v8"/></svg>
      <div class="stat-value">10088</div><div class="stat-label">Customers</div>
    </div>
    <div class="stat-card" style="left:701px">
      <svg width="28" height="32" viewBox="0 0 28 32" fill="none" stroke="#a3c93a" stroke-width="1.5"><rect x="2" y="15" width="6" height="14"/><path d="M8 16l5-7V3a2 2 0 0 1 3 1v9h7a2 2 0 0 1 2 2l-2 12a2 2 0 0 1-2 2H8"/></svg>
      <div class="stat-value">10279</div><div class="stat-label">Likes</div>
    </div>
    <div class="stat-card" style="left:846px">
      <svg width="28" height="32" viewBox="0 0 28 32" fill="none" stroke="#a3c93a" stroke-width="1.5"><path d="M14 27S3 20 3 12a5.5 5.5 0 0 1 11-2 5.5 5.5 0 0 1 11 2c0 8-11 15-11 15z"/></svg>
      <div class="stat-value">4406</div><div class="stat-label">Followers</div>
    </div>
  </section>

  <section class="farms-band">
    <div class="natural-badge" role="img" aria-label="Natural food badge"></div>
    <h2 class="farms-title">All of our foods come from ecology farms</h2>
    <ul class="farms-points">
      <li>In commodo est quis enim iaculis mattis</li>
      <li>Etiam id eros vel lacus semper fermentum</li>
      <li>Quisque a nunc ante</li>
    </ul>
    <div class="butcher-photo" role="img" aria-label="Photo of a smiling butcher holding a tray of raw meat"></div>
  </section>

  <footer class="site-footer">
    <ul class="footer-nav">
      <li>How it works</li><li>About</li><li>Register</li><li>Login</li>
    </ul>
    <p class="copyright">Copyright © 2016 by Fieldhand. All Right Reserved.</p>
  </footer>
</body>
</html>
```